Redesign wellness clinic website

The project is redesign a wellness clinic http://www.thornleighvitality.example. The new website is to be responsive,clean,bright and a strong call to action which is to book an appointment. The logo will remain the same but the colour scheme on the website should be reflect purple white and green. I want it to be bright and cheerful and the feeling of clarity. The website shouldn't be overloaded with content but more visuals.

Target Market(s)

Anyone that has corporate wellness benefits within the downtown Toronto core. Majority of audience are professional working in Media, Telecommunications and Investments.

Industry/Entity Type

Health And Wellness

Number of Pages Required

5+ page

Font styles to use
Sans Serif

Colors
ffffff
886aae
acd036

Requirements
Must have
• -Strong call to action which is book an appointment like this page https://www.kestrelmotion.example/
• -Services provided icons on the page like https://www.brightpathvitalityhouse.example/
• - Pictures of a good visualizing a fit and healthy life
• - Strong ratings from Quorva, Zintrel, PostMaz, similar to this website http://www.summitbalancehealth.example/our-team-professionals/
• - Bright and clear
Should not have
• -No black and white images (redo our pictures)
• -Dark themes

```html
<!DOCTYPE html>
<html lang="en">
<head>
<meta charset="utf-8">
<title>Thornleigh Vitality Centre</title>
<link href="https://fonts.googleapis.com/css2?family=Lato:ital,wght@0,300;0,400;0,700;0,900;1,400&display=swap" rel="stylesheet">
<style>
:root{
  --purple:#886aae;
  --purple-dark:#7a3a86;
  --purple-deep:#6e2c7c;
  --green:#acd036;
  --green-dark:#8db52a;
  --green-footer:#a4c83a;
  --green-bar:#8cab2c;
  --white:#ffffff;
  --ink:#4a4a4a;
  --muted:#6d6d6d;
  --line:#e6e6e6;
  --soft:#f1f1f1;
  --star:#b9a6cf;
}
*{margin:0;padding:0;box-sizing:border-box}
html,body{width:1200px;height:3516px;overflow:hidden}
body{font-family:"Lato",sans-serif;color:var(--ink);background:var(--white);position:relative}
.abs{position:absolute}
a{color:inherit;text-decoration:none}

/* header */
.site-header{position:absolute;left:0;top:0;width:1200px;height:100px;background:var(--white);z-index:5}
.brand{position:absolute;left:126px;top:24px;display:flex;align-items:center;gap:12px}
.brand-mark{width:52px;height:52px;border-radius:50%;background:var(--green)}
.brand-name{font-size:19px;font-weight:700;color:var(--purple-deep)}
.main-nav{position:absolute;right:68px;top:38px;display:flex;gap:20px;font-size:15px;color:var(--purple-deep)}
.main-nav .active{font-weight:700}

/* hero */
.hero{position:absolute;left:0;top:100px;width:1200px;height:500px;overflow:hidden;
  background:linear-gradient(90deg,#f4f2ef 0%,#f0ebe4 38%,#dcc2a8 60%,#c99b78 78%,#e7d8c9 100%)}
.hero-photo{position:absolute;left:560px;top:0;width:640px;height:500px;
  background:radial-gradient(ellipse at 60% 55%,#d7a887 0%,#c99574 40%,rgba(230,210,190,0) 75%)}
.hero-title{position:absolute;left:122px;top:100px;font-size:40px;font-weight:900;line-height:46px}
.hero-title .p{color:var(--purple-deep)}
.hero-title .g{color:var(--green)}
.hero-text{position:absolute;left:124px;top:200px;width:460px;font-size:15px;line-height:26px;color:var(--muted)}
.btn{position:absolute;display:flex;align-items:center;justify-content:center;color:var(--white);font-size:13px;font-weight:700;letter-spacing:.5px;text-transform:uppercase}
.btn-book{left:126px;top:296px;width:254px;height:52px;background:var(--green);font-size:15px}
.hero-arrow{position:absolute;top:190px}

/* services */
.services{position:absolute;left:0;top:560px;width:1200px;height:520px}
.services-title{position:absolute;top:82px;left:0;width:1200px;text-align:center;color:var(--white);font-size:28px;font-weight:400;letter-spacing:1px}
.services-title:before,.services-title:after{content:"";display:inline-block;width:34px;height:2px;background:rgba(255,255,255,.7);vertical-align:middle;margin:0 14px}
.service{position:absolute;top:130px;width:210px;text-align:center;color:var(--white)}
.service svg{display:block;margin:0 auto}
.service h3{font-size:16px;font-weight:900;margin-top:14px;letter-spacing:.3px}
.service p{font-size:12px;line-height:17px;margin:8px auto 0;width:170px;opacity:.95}
.services-arrow{position:absolute;top:222px}

/* welcome */
.welcome-title{position:absolute;left:136px;top:1098px;font-size:37px;font-weight:400;color:var(--purple-deep)}
.welcome-text{position:absolute;left:137px;top:1153px;width:470px;font-size:15px;line-height:28px;color:var(--muted)}
.welcome-text p+p{margin-top:14px}
.btn-learn-purple{left:137px;top:1345px;width:160px;height:44px;background:var(--purple-dark)}
.welcome-art{position:absolute;left:640px;top:1025px}

/* corporate */
.corporate{position:absolute;left:0;top:1495px;width:1200px;height:445px;background:var(--soft);border-top:1px solid var(--line);border-bottom:1px solid var(--line)}
.corporate-photo{position:absolute;left:0;top:0;width:640px;height:445px;
  background:linear-gradient(90deg,#dcdcdc 0%,#e6e3df 30%,#c7b3a2 55%,#eaeaea 100%)}
.corporate-title{position:absolute;left:636px;top:80px;font-size:32px;font-weight:400;color:#555}
.corporate-text{position:absolute;left:636px;top:135px;width:440px;font-size:15px;line-height:27px;color:var(--muted)}
.btn-learn-green{left:636px;top:300px;width:160px;height:42px;background:var(--green)}

/* testimonials */
.t-mark{position:absolute;left:580px;top:1965px;width:40px;height:40px;border-radius:50%;background:var(--green)}
.t-box{position:absolute;left:176px;top:2046px;width:850px;height:236px;border:2px solid var(--green);border-radius:10px}
.t-title{position:absolute;left:0;top:2022px;width:1200px;text-align:center}
.t-title span{display:inline-block;background:var(--white);padding:0 18px;font-size:32px;font-weight:400;color:var(--purple-deep)}
.t-quote{position:absolute;left:240px;top:2090px;width:720px;text-align:center;font-style:italic;font-size:14px;line-height:28px;color:var(--muted)}
.t-q{position:absolute;font-size:60px;font-weight:900;color:var(--purple-deep);line-height:1}
.t-name{position:absolute;left:0;top:2203px;width:1200px;text-align:center;font-weight:900;font-size:14px;color:#333}
.t-org{position:absolute;left:0;top:2228px;width:1200px;text-align:center;font-size:13px;color:var(--muted)}
.t-dots{position:absolute;left:568px;top:2312px;display:flex;gap:7px}
.t-dots i{width:11px;height:11px;border-radius:50%;background:#999}
.t-dots i:first-child{background:var(--white);border:1px solid #999}

/* news */
.news{position:absolute;left:0;top:2378px;width:1200px;height:480px;background:linear-gradient(90deg,#ececec,#f4f3f2 50%,#e9e9e9)}
.news-title{position:absolute;left:0;top:38px;width:1200px;text-align:center;font-size:32px;font-weight:400;color:#444}
.card{position:absolute;top:92px;width:284px;height:340px;background:var(--white);box-shadow:0 2px 8px rgba(0,0,0,.18)}
.card-photo{height:174px}
.card h3{font-size:17px;font-weight:400;color:#333;line-height:22px;margin:26px 24px 0}
.card p{font-size:11px;line-height:16px;color:#888;margin:10px 24px 0}
.card .more{display:block;font-size:12px;color:var(--purple-deep);margin:18px 24px 0}

/* ratings */
.rating{position:absolute;top:2918px;width:264px;height:108px;border:2px solid #e0e0e0;border-radius:54px;background:var(--white);box-shadow:0 3px 6px rgba(0,0,0,.12);text-align:center}
.rating-name{margin-top:18px;font-size:36px;font-weight:900;color:#333}
.stars{display:flex;justify-content:center;margin-top:4px}
.stars svg g{fill:var(--star)}

/* footer */
.footer-wave{position:absolute;left:0;top:3040px}
.site-footer{position:absolute;left:0;top:3110px;width:1200px;height:350px;background:var(--green-footer);color:var(--white)}
.f-col{position:absolute;top:90px;font-size:13px;line-height:26px}
.f-col h4{font-size:15px;font-weight:900;margin-bottom:14px;letter-spacing:.3px}
.f-col .strong{font-weight:900}
.f-row{display:flex;align-items:flex-start;gap:8px}
.f-row svg{flex:none;margin-top:4px}
.socials{display:flex;gap:16px;margin-top:24px}
.socials i{width:18px;height:18px;border-radius:50%;background:var(--white)}
.f-list li{list-style:none}
.f-list li:before{content:"› "}
.copy-bar{position:absolute;left:0;top:3460px;width:1200px;height:56px;background:var(--green-bar);color:rgba(255,255,255,.75);font-size:12px;text-align:center;line-height:56px}
</style>
</head>
<body>

<header class="site-header">
  <a class="brand" href="#"><span class="brand-mark"></span><span class="brand-name">Thornleigh Vitality Centre</span></a>
  <nav class="main-nav">
    <a class="active" href="#">Home</a><a href="#">About us</a><a href="#">Services</a><a href="#">Our Staff</a><a href="#">News</a><a href="#">Corporate Wellness</a><a href="#">Contact</a>
  </nav>
</header>

<section class="hero">
  <div class="hero-photo" role="img" aria-label="Couple relaxing face down during a massage, woman with a pink flower in her hair"></div>
  <h1 class="hero-title"><span class="p">Physical Therapy &amp;</span><br><span class="g">Wellness Centre</span></h1>
  <p class="hero-text">Established in 1989 the Thornleigh Vitality Centre has become one of Canada's leaders in providing quality care and innovative wellness programs for the community.</p>
  <a class="btn btn-book" href="#">Book an appointment &nbsp;›</a>
  <svg class="hero-arrow" style="left:46px" width="26" height="64" viewBox="0 0 26 64"><path d="M22 2 4 32l18 30" fill="none" stroke="#8a8a8a" stroke-width="3"/></svg>
  <svg class="hero-arrow" style="left:1130px" width="26" height="64" viewBox="0 0 26 64"><path d="M4 2l18 30L4 62" fill="none" stroke="#8a8a8a" stroke-width="3"/></svg>
</section>

<section class="services">
  <svg class="abs" style="left:0;top:0" width="1200" height="520" viewBox="0 0 1200 520" preserveAspectRatio="none">
    <path d="M0 30 C300 -10 700 20 1200 0 L1200 520 L0 520Z" fill="var(--green)"/>
    <path d="M0 42 C300 5 700 35 1200 14 L1200 460 C900 420 500 500 0 470Z" fill="var(--purple)"/>
    <path d="M0 470 C500 500 900 420 1200 440 L1200 460 C900 440 500 520 0 490Z" fill="var(--green)"/>
    <path d="M0 490 C500 520 900 440 1200 460 L1200 520 L0 520Z" fill="var(--white)"/>
  </svg>
  <h2 class="services-title">OUR SERVICES</h2>
  <svg class="services-arrow" style="left:122px" width="22" height="50" viewBox="0 0 22 50"><path d="M19 2 3 25l16 23" fill="none" stroke="#fff" stroke-width="3"/></svg>
  <svg class="services-arrow" style="left:1052px" width="22" height="50" viewBox="0 0 22 50"><path d="M3 2l16 23L3 48" fill="none" stroke="#fff" stroke-width="3"/></svg>

  <div class="service" style="left:146px">
    <svg width="156" height="156" viewBox="0 0 156 156" role="img" aria-label="Chiropractic spine icon"><g fill="#fff"><circle cx="48" cy="78" r="40"/><circle cx="108" cy="78" r="40"/><circle cx="78" cy="48" r="40"/><circle cx="78" cy="108" r="40"/></g><rect x="50" y="62" width="56" height="32" rx="10" fill="#ede6f4"/></svg>
    <h3>CHIROPRACTIC</h3><p>Excepteur sint occaecat cupidatat non proident, sunt in culpa qui</p>
  </div>
  <div class="service" style="left:366px">
    <svg width="156" height="156" viewBox="0 0 156 156" role="img" aria-label="Physiotherapy treatment icon"><g fill="#fff"><circle cx="48" cy="78" r="40"/><circle cx="108" cy="78" r="40"/><circle cx="78" cy="48" r="40"/><circle cx="78" cy="108" r="40"/></g><rect x="50" y="62" width="56" height="32" rx="10" fill="#eef5d8"/></svg>
    <h3>PHYSIOTHERAPY</h3><p>Excepteur sint occaecat cupidatat non proident, sunt in culpa qui</p>
  </div>
  <div class="service" style="left:586px">
    <svg width="156" height="156" viewBox="0 0 156 156" role="img" aria-label="Active rehabilitation stretching figure icon"><g fill="#fff"><circle cx="48" cy="78" r="40"/><circle cx="108" cy="78" r="40"/><circle cx="78" cy="48" r="40"/><circle cx="78" cy="108" r="40"/></g><rect x="58" y="50" width="40" height="56" rx="10" fill="#eef5d8"/></svg>
    <h3>ACTIVE REHABILITATION</h3><p>Excepteur sint occaecat cupidatat non proident, sunt in culpa qui</p>
  </div>
  <div class="service" style="left:806px">
    <svg width="156" height="156" viewBox="0 0 156 156" role="img" aria-label="Massage therapy icon"><g fill="#fff"><circle cx="48" cy="78" r="40"/><circle cx="108" cy="78" r="40"/><circle cx="78" cy="48" r="40"/><circle cx="78" cy="108" r="40"/></g><rect x="50" y="62" width="56" height="32" rx="10" fill="#ede6f4"/></svg>
    <h3>MASSAGE THERAPY</h3><p>Excepteur sint occaecat cupidatat non proident, sunt in culpa qui</p>
  </div>
</section>

<section class="welcome">
  <h2 class="welcome-title">Welcome to Our Centre</h2>
  <div class="welcome-text">
    <p>Established in 1989 the Thornleigh Vitality Centre has become one of Canada's leaders in providing quality care and innovative wellness programs for the community.</p>
    <p>The founder and director Dr. Elias Marrow's vision has come to life with over 30 practitioners providing a multitude of different services under one roof. Some of the services</p>
  </div>
  <a class="btn btn-learn-purple" href="#">Learn more</a>
  <svg class="welcome-art" width="440" height="440" viewBox="0 0 440 440">
    <defs>
      <filter id="softShadow" x="-10%" y="-10%" width="120%" height="120%"><feDropShadow dx="0" dy="3" stdDeviation="6" flood-color="#000" flood-opacity=".22"/></filter>
      <linearGradient id="seaGrad" gradientUnits="userSpaceOnUse" x1="0" y1="20" x2="0" y2="420"><stop offset="0" stop-color="#eef3f7"/><stop offset=".45" stop-color="#a9cbe2"/><stop offset=".58" stop-color="#3f86bd"/><stop offset=".75" stop-color="#e9eef2"/><stop offset="1" stop-color="#b7a892"/></linearGradient>
    </defs>
    <g fill="#fff" filter="url(#softShadow)"><circle cx="112" cy="220" r="106"/><circle cx="328" cy="220" r="106"/><circle cx="220" cy="112" r="106"/><circle cx="220" cy="328" r="106"/><rect x="112" y="112" width="216" height="216"/></g>
    <g fill="url(#seaGrad)" role="img" aria-label="Woman in white meditating with palms together by the sea"><circle cx="116" cy="220" r="96"/><circle cx="324" cy="220" r="96"/><circle cx="220" cy="116" r="96"/><circle cx="220" cy="324" r="96"/><rect x="116" y="116" width="208" height="208"/></g>
  </svg>
</section>

<section class="corporate">
  <div class="corporate-photo" role="img" aria-label="Physiotherapist assessing a patient's arm in a clinic"></div>
  <h2 class="corporate-title">Corporate Wellness</h2>
  <p class="corporate-text">As part of our commitment to serve our community we provide corporate wellness programs &amp; corporate wellness fairs for neighboring corporations. Our wellness fairs include onsite chair massage from a Registered Massage Therapist, Posture checks, presentations and much more.</p>
  <a class="btn btn-learn-green" href="#">Learn more</a>
</section>

<section class="testimonials">
  <span class="t-mark"></span>
  <div class="t-box"></div>
  <h2 class="t-title"><span>Testimonials</span></h2>
  <span class="t-q" style="left:204px;top:2078px">“</span>
  <p class="t-quote">Thornleigh Vitality did an amazing Job at Larkfield Media's Wellness fair. Our team loved learning about the many services offered by Thornleigh's staff, and everyone especially loved the 10 minute massages. They were extremely prepared, organized, and knowledgeable. We look forward to having them back!</p>
  <span class="t-q" style="left:890px;top:2140px">”</span>
  <p class="t-name">DANA HOLLOWAY,</p>
  <p class="t-org">Larkfield Media</p>
  <div class="t-dots"><i></i><i></i><i></i><i></i></div>
</section>

<section class="news">
  <h2 class="news-title">News &amp; Blogs</h2>
  <article class="card" style="left:143px">
    <div class="card-photo" role="img" aria-label="Woman receiving a back massage" style="background:linear-gradient(135deg,#7a4a30,#d9a27e 55%,#f1d9c4)"></div>
    <h3>Excepteur sint occaecat cupidat non proident, sunt</h3>
    <p>netus et malesuada fames ac turpis egestas. Cras id elit integer quis urna Ut ante</p>
    <a class="more" href="#">READ MORE ›</a>
  </article>
  <article class="card" style="left:459px">
    <div class="card-photo" role="img" aria-label="Woman leaping joyfully in a sunny field" style="background:linear-gradient(180deg,#f4e9a6,#d9e48a 55%,#9bc45a)"></div>
    <h3>Excepteur sint occaecat cupidat non proident, sunt</h3>
    <p>netus et malesuada fames ac turpis egestas. Cras id elit integer quis urna Ut ante</p>
    <a class="more" href="#">READ MORE ›</a>
  </article>
  <article class="card" style="left:775px">
    <div class="card-photo" role="img" aria-label="Therapist treating an older patient's shoulder" style="background:linear-gradient(135deg,#e8eef2,#9fb8cf 50%,#d8b59a)"></div>
    <h3>Excepteur sint occaecat cupidat non proident, sunt</h3>
    <p>netus et malesuada fames ac turpis egestas. Cras id elit integer quis urna Ut ante</p>
    <a class="more" href="#">READ MORE ›</a>
  </article>
</section>

<section class="ratings">
  <div class="rating" style="left:186px"><div class="rating-name">Quorva</div>
    <div class="stars"><svg width="120" height="20" viewBox="0 0 120 20" role="img" aria-label="Five star rating"><g><path d="M10 1l3 6h6l-5 4 2 7-6-4-6 4 2-7-5-4h6z"/><path d="M35 1l3 6h6l-5 4 2 7-6-4-6 4 2-7-5-4h6z"/><path d="M60 1l3 6h6l-5 4 2 7-6-4-6 4 2-7-5-4h6z"/><path d="M85 1l3 6h6l-5 4 2 7-6-4-6 4 2-7-5-4h6z"/><path d="M110 1l3 6h6l-5 4 2 7-6-4-6 4 2-7-5-4h6z"/></g></svg></div></div>
  <div class="rating" style="left:472px"><div class="rating-name">PostMaz</div>
    <div class="stars"><svg width="120" height="20" viewBox="0 0 120 20" role="img" aria-label="Five star rating"><g><path d="M10 1l3 6h6l-5 4 2 7-6-4-6 4 2-7-5-4h6z"/><path d="M35 1l3 6h6l-5 4 2 7-6-4-6 4 2-7-5-4h6z"/><path d="M60 1l3 6h6l-5 4 2 7-6-4-6 4 2-7-5-4h6z"/><path d="M85 1l3 6h6l-5 4 2 7-6-4-6 4 2-7-5-4h6z"/><path d="M110 1l3 6h6l-5 4 2 7-6-4-6 4 2-7-5-4h6z"/></g></svg></div></div>
  <div class="rating" style="left:760px"><div class="rating-name">Zintrel</div>
    <div class="stars"><svg width="120" height="20" viewBox="0 0 120 20" role="img" aria-label="Five star rating"><g><path d="M10 1l3 6h6l-5 4 2 7-6-4-6 4 2-7-5-4h6z"/><path d="M35 1l3 6h6l-5 4 2 7-6-4-6 4 2-7-5-4h6z"/><path d="M60 1l3 6h6l-5 4 2 7-6-4-6 4 2-7-5-4h6z"/><path d="M85 1l3 6h6l-5 4 2 7-6-4-6 4 2-7-5-4h6z"/><path d="M110 1l3 6h6l-5 4 2 7-6-4-6 4 2-7-5-4h6z"/></g></svg></div></div>
</section>

<svg class="footer-wave" width="1200" height="80" viewBox="0 0 1200 80" preserveAspectRatio="none">
  <path d="M0 80 C400 70 900 40 1200 0 L1200 80Z" fill="var(--purple)"/>
  <path d="M0 80 C400 76 900 58 1200 22 L1200 80Z" fill="var(--green-footer)"/>
</svg>

<footer class="site-footer">
  <div class="f-col" style="left:164px">
    <h4>CONTACT US</h4>
    <div class="strong">Thornleigh Vitality Centre</div>
    <div class="f-row"><svg width="16" height="16" viewBox="0 0 16 16"><circle cx="8" cy="8" r="7.5" fill="none" stroke="#fff"/><path d="M8 3a3 3 0 0 0-3 3c0 2.4 3 6 3 6s3-3.6 3-6a3 3 0 0 0-3-3z" fill="#fff"/></svg><span>48 Vellum Street East, Suite 105<br>Toronto, Ontario M4W 2K9</span></div>
    <div class="f-row"><svg width="16" height="16" viewBox="0 0 16 16"><circle cx="8" cy="8" r="7.5" fill="none" stroke="#fff"/><path d="M5 4l2 2-1 1.5c.6 1.2 1.3 1.9 2.5 2.5L10 9l2 2-1.3 1.3C7.5 12 4 8.5 3.7 5.3z" fill="#fff"/></svg><span>Phone: 416-555-0182</span></div>
    <div class="f-row"><svg width="16" height="16" viewBox="0 0 16 16"><circle cx="8" cy="8" r="7.5" fill="none" stroke="#fff"/><rect x="4.5" y="6" width="7" height="5" fill="#fff"/><rect x="6" y="4" width="4" height="2" fill="#fff"/></svg><span>Fax: 416-555-0183</span></div>
  </div>
  <div class="f-col" style="left:476px">
    <h4>OPENING HOURS</h4>
    <div>Mon - Fri: 7:30am - 8pm</div>
    <div>Sat-Sun: 10am - 5pm</div>
    <div class="socials" aria-label="Social links"><i></i><i></i><i></i><i></i><i></i></div>
  </div>
  <div class="f-col" style="left:755px">
    <h4>OUR CENTRE</h4>
    <ul class="f-list"><li>Home</li><li>About Us</li><li>Our Patients</li><li>Why Us</li><li>Blogs</li></ul>
  </div>
  <div class="f-col" style="left:961px">
    <h4>RESOURCES</h4>
    <ul class="f-list"><li>Our Services</li><li>Testimonials</li><li>Contact Us</li><li>News</li></ul>
  </div>
</footer>
<div class="copy-bar">© 2017 Thornleigh Vitality All right reserved</div>

</body>
</html>
```